Brevak label design

Redesign cafe range label for lightly carbonated fruit sodas.
Existing label has not worked in the market place and needs to appeal to 18-40 year olds with an active healthy lifestyle.

Product will remain in current 330ml glass bottle and flavour profile will include current range, sparkling water. It is preferred to maintain a body label only but will consider neck label as well. No over cap concepts will be considered..

Attached final shows brand progress. It has lost its way and needs reinvigorating.

Reason: I have extended the deadline to get proper feed back from others on the designs. Thank you all for your submissions so far. Ted

```html
<!DOCTYPE html>
<html lang="en">
<head>
<meta charset="utf-8">
<title>Brevak Fruit Drink Label</title>
<link rel="stylesheet" href="https://fonts.googleapis.com/css2?family=Fondamento&display=swap">
<style>
  :root {
    --paper: #ffffff;
    --ink: #1e1c1c;
    --citrus: #f99a3e;
    --berry: #b51fb8;
  }
  html, body {
    margin: 0;
    padding: 0;
    width: 1200px;
    height: 999px;
    overflow: hidden;
    background: var(--paper);
  }
  .label {
    position: relative;
    width: 1200px;
    height: 999px;
    background: var(--paper);
    font-family: "Fondamento", serif;
    color: var(--ink);
  }
  .brand {
    position: absolute;
    left: 655px;
    top: 372px;
    display: flex;
    align-items: center;
    gap: 14px;
  }
  .brand-dot {
    width: 36px;
    height: 36px;
    border-radius: 50%;
    background: var(--ink);
  }
  .brand-name {
    font-size: 46px;
    line-height: 1;
    color: var(--ink);
  }
  .flow-band {
    position: absolute;
    left: 497px;
    top: 474px;
    width: 350px;
    height: 58px;
    border-radius: 29px;
    background: linear-gradient(170deg, var(--citrus) 0%, var(--berry) 50%, var(--citrus) 100%);
  }
  .product-name {
    position: absolute;
    left: 432px;
    top: 538px;
    margin: 0;
    font-size: 90px;
    font-weight: 400;
    font-style: italic;
    line-height: 1;
    letter-spacing: 1px;
    white-space: nowrap;
  }
  .product-note {
    position: absolute;
    left: 722px;
    top: 627px;
    margin: 0;
    font-size: 16.5px;
    font-style: italic;
    white-space: nowrap;
  }
  .product-volume {
    position: absolute;
    left: 778px;
    top: 656px;
    margin: 0;
    font-size: 29px;
    font-style: italic;
    white-space: nowrap;
  }
</style>
</head>
<body>
  <main class="label">
    <div class="brand">
      <span class="brand-dot"></span>
      <span class="brand-name">Brevak</span>
    </div>

    <div class="flow-band" role="img" aria-label="Flowing orange and purple ribbon ornament"></div>

    <h1 class="product-name">Fruit Drink</h1>
    <p class="product-note">Lightly Carbonated</p>
    <p class="product-volume">330ml</p>
  </main>
</body>
</html>
```